Global Nano Technology Surface Protection company needs a new logo and cards

We are a Global company that will apply nanotechnology coatings on surfaces to prevent growth and spread of bacteria, viruses, mold etc. We deal with large corporates, airlines, hospitals and schools so we are after a new modern, simple and clean look that will have great visual impact.
We a company that is focused on prevention and protection.

Company name, Quorvane Systems Worldwide

Subtext, Antimicrobial Surface Protection

Logo, QVSW or QSW

Target Market(s)

Hospitals, Transport agencies, Airlines, Corporate entities

Industry/Entity Type

Protection

Contact Information for Business Card

Logo, QVSW or QSW
www.qvsw-example.us
Derek Holloway
+64290536218
tidyshieldnz@mailbox-example.com

Logo Text

QVSW

Requirements
Must have
• Simple clean look
Should not have
• Nothing too messy

```html
<!DOCTYPE html>
<html lang="en">
<head>
<meta charset="utf-8">
<title>Quorvane Systems Worldwide — Business Cards</title>
<link href="https://fonts.googleapis.com/css2?family=Montserrat:wght@300;400;600;700&display=swap" rel="stylesheet">
<style>
  :root {
    --bg: #c9c9c9;
    --card-black: #050505;
    --brand-blue: #2a9bdc;
    --band-blue: #0b6a94;
    --logo-grey: #3d3d3d;
    --paper: #ffffff;
    --ribbon-shadow: #8a8a8a;
  }
  * { box-sizing: border-box; margin: 0; padding: 0; }
  html, body {
    width: 1200px; height: 1000px; overflow: hidden;
    background: var(--bg);
    font-family: "Montserrat", sans-serif;
  }
  .card {
    position: absolute; left: 210px;
    width: 780px; height: 446px;
    overflow: hidden;
    box-shadow: 0 6px 18px rgba(0,0,0,.25);
  }
  .card--front { top: 40px; background: var(--card-black); }
  .card--back { top: 514px; background: var(--card-black); }

  .front-wordmark {
    position: absolute; left: 0; right: 0; top: 118px;
    text-align: center;
    font-weight: 700; font-size: 104px; letter-spacing: 4px;
    color: var(--brand-blue); line-height: 1;
  }
  .ribbon { position: absolute; left: 110px; top: 262px; width: 560px; height: 56px; }
  .ribbon-text {
    position: absolute; left: 0; right: 0; top: 273px;
    text-align: center;
    font-weight: 600; font-size: 24px; letter-spacing: 1px;
    color: #111;
  }

  .back-shapes { position: absolute; inset: 0; }
  .back-wordmark {
    position: absolute; left: 40px; top: 170px; width: 300px;
    text-align: center;
    font-weight: 700; font-size: 74px; letter-spacing: 3px;
    color: var(--logo-grey); line-height: 1;
  }
  .details {
    position: absolute; right: 40px; top: 74px;
    text-align: right; color: var(--paper);
  }
  .company-name { font-weight: 700; font-size: 21px; letter-spacing: 1px; line-height: 1.2; }
  .company-region { font-weight: 300; font-size: 26px; letter-spacing: 2px; line-height: 1.15; }
  .person-name { margin-top: 16px; font-weight: 700; font-size: 29px; letter-spacing: 2px; line-height: 1.1; }
  .person-role { font-weight: 400; font-size: 18px; letter-spacing: 3px; }
  .contacts { margin-top: 20px; list-style: none; }
  .contact {
    display: flex; justify-content: flex-end; align-items: center; gap: 10px;
    font-size: 16px; letter-spacing: 0.6px; height: 36px; white-space: nowrap;
  }
  .contact svg { width: 28px; height: 28px; flex: none; }
</style>
</head>
<body>

<section class="card card--front" aria-label="Card front">
  <div class="front-wordmark">QVSW</div>
  <svg class="ribbon" viewBox="0 0 560 56" aria-hidden="true">
    <polygon points="0,6 560,6 560,50 0,50" fill="var(--paper)"/>
    <polygon points="-10,2 10,2 32,28 10,54 -10,54 12,28" fill="var(--ribbon-shadow)"/>
    <polygon points="18,6 34,6 52,28 34,50 18,50 36,28" fill="#111"/>
    <polygon points="570,2 550,2 528,28 550,54 570,54 548,28" fill="var(--ribbon-shadow)"/>
    <polygon points="542,6 526,6 508,28 526,50 542,50 524,28" fill="#111"/>
  </svg>
  <div class="ribbon-text">Antimicrobial Surface Protection</div>
</section>

<section class="card card--back" aria-label="Card back">
  <svg class="back-shapes" viewBox="0 0 780 446" aria-hidden="true">
    <rect x="0" y="0" width="780" height="40" fill="var(--band-blue)"/>
    <rect x="0" y="384" width="780" height="62" fill="var(--band-blue)"/>
    <polygon points="0,40 300,40 372,232 220,384 0,384" fill="var(--paper)"/>
  </svg>
  <div class="back-wordmark">QVSW</div>

  <div class="details">
    <p class="company-name">Quorvane Systems</p>
    <p class="company-region">Worldwide</p>
    <p class="person-name">Derek Holloway</p>
    <p class="person-role">managing director</p>
    <ul class="contacts">
      <li class="contact">+64290536218
        <svg viewBox="0 0 30 30" aria-hidden="true"><circle cx="15" cy="15" r="13" fill="none" stroke="var(--brand-blue)" stroke-width="2"/><path d="M8 13 q7-6 14 0 v2 h-4 v-2 h-6 v2 h-4z M10 16 h10 v6 h-10z" fill="var(--brand-blue)"/></svg>
      </li>
      <li class="contact">tidyshieldnz@mailbox-example.com
        <svg viewBox="0 0 30 30" aria-hidden="true"><circle cx="15" cy="15" r="13" fill="none" stroke="var(--brand-blue)" stroke-width="2"/><rect x="8" y="10" width="14" height="10" fill="var(--brand-blue)"/><path d="M8 10 l7 6 l7-6" fill="none" stroke="var(--card-black)" stroke-width="1.5"/></svg>
      </li>
      <li class="contact">www.qvsw-example.us
        <svg viewBox="0 0 30 30" aria-hidden="true"><circle cx="15" cy="15" r="13" fill="none" stroke="var(--brand-blue)" stroke-width="2"/><circle cx="15" cy="15" r="8" fill="none" stroke="var(--brand-blue)" stroke-width="1.5"/><ellipse cx="15" cy="15" rx="3.5" ry="8" fill="none" stroke="var(--brand-blue)" stroke-width="1.5"/><path d="M7 15 h16 M9 11 h12 M9 19 h12" stroke="var(--brand-blue)" stroke-width="1.2"/></svg>
      </li>
    </ul>
  </div>
</section>

</body>
</html>
```